Pharmaceutical Manufacturing Services Advertisement

We need a new full page advertisement designed for publication in international magazines. We are a custom pharmaceutical manufacturing company and we help biotechnology companies scale up their drug development for clinical trials. The products we help manufacture are therapeutics for global healthcare problems.

Target Market(s)

Verott Bio is a privately owned contract development manufacturing organisation (CDMO) headquartered in Darra, QLD, Australia.

Our mission is to is to be a global leader in development and in the provision of contract manufacturing for active pharmaceutical ingredient processes.

Why we do what we Do:

To help advance Biotechnology Companies so that they can deliver innovative therapeutics
~ enabling patients to live longer, healthier and happier lives
~ which solves worldwide health problems

Verott Bio’s role is to develop, implement and scale up the production to deliver biologic medicines for patients in partnership with the biotechnology companies.

Industry/Entity Type

Biotechnology

Font styles to use
Sans Serif

Colors

Designer to choose colors to be used in the design.

Requirements
Must have
• Please see the script on the Word document. There are 4 optional Header Taglines. Additional ideas for multiple designs for the taglines welcomed.
• However preference is for either of the first two:
• 1. Building your vision for better healthcare
• 2. Bridging your vision for better healthcare
• File Specs:
• • All artwork should be submitted as high-resolution (300 min. dpi), press-ready PDF files
• • CMYK color only
• • Full page 8.25” x 10.812”; 209.55 x 274.62 mm
• • Live Area for all sizes: 0.25” (6.35 mm) inside the trim
• • Bleed Area for all sizes: Extends 0.125” (3.175 mm) from trim
Nice to have
• Modern Science look to inspire biotechnology companies to work with us.
• Search for images to use by keyword "recombinant dna"

```html
<!DOCTYPE html>
<html lang="en">
<head>
<meta charset="utf-8">
<title>Verott Bio – Full Page Advertisement</title>
<link rel="stylesheet" href="https://fonts.googleapis.com/css2?family=Barlow+Condensed:wght@600;700&family=Archivo:wght@300;400;600;700&display=swap">
<style>
  :root {
    --navy: #02578a;
    --lime: #c3d322;
    --ink: #111111;
    --body: #2a2a2a;
    --stage: #d2d3d5;
    --paper: #ffffff;
  }
  * { margin: 0; padding: 0; box-sizing: border-box; }
  html, body { width: 1200px; height: 1200px; overflow: hidden; background: var(--stage); }
  .canvas { position: relative; width: 1200px; height: 1200px; }
  .ad-page {
    position: absolute; left: 168px; top: 34px; width: 864px; height: 1132px;
    background: var(--paper); overflow: hidden;
    font-family: "Archivo", "Helvetica Neue", Arial, sans-serif;
  }
  .rule { position: absolute; left: 0; width: 100%; height: 23px; background: var(--navy); }
  .rule--top { top: 0; }
  .rule--bottom { bottom: 0; }

  .headline { position: absolute; left: 49px; top: 62px; font-family: "Barlow Condensed", "Arial Narrow", sans-serif; font-weight: 700; line-height: 1; text-transform: uppercase; }
  .headline__big { display: block; color: var(--navy); font-size: 116px; letter-spacing: 0.5px; }
  .headline__mid { display: block; color: var(--lime); font-size: 60px; margin: 2px 0 0 1px; letter-spacing: 0.5px; }
  .headline__big--second { margin-top: 0; }

  .strap {
    position: absolute; left: 0; top: 344px; width: 100%; height: 47px;
    background: var(--lime); color: var(--ink);
    font-weight: 700; font-size: 28.5px; line-height: 47px; text-align: center; letter-spacing: -0.2px;
  }

  .intro { position: absolute; left: 51px; top: 409px; width: 762px; color: var(--body); font-size: 16px; line-height: 21px; font-weight: 300; text-align: justify; }
  .intro p + p { margin-top: 20px; }

  .tab {
    position: absolute; left: 0; width: 312px; height: 34px; background: var(--navy);
    clip-path: polygon(0 0, 295px 0, 100% 100%, 0 100%);
    color: #fff; font-weight: 700; font-size: 24px; line-height: 34px; padding-left: 54px;
  }
  .tab--products { top: 624px; }
  .tab--services { top: 804px; }

  .offer-list { position: absolute; left: 55px; list-style: none; color: var(--ink); font-size: 20px; font-weight: 300; line-height: 23.6px; }
  .offer-list li { position: relative; padding-left: 60px; white-space: nowrap; }
  .offer-list li::before { content: ""; position: absolute; left: 6px; top: 9px; width: 7px; height: 7px; border-radius: 50%; background: var(--ink); }
  .offer-list--products { top: 677px; }
  .offer-list--services { top: 857px; }

  .feature-photo { position: absolute; left: 441px; top: 573px; width: 398px; height: 398px; }

  .contact { position: absolute; left: 48px; top: 1005px; font-size: 21.5px; line-height: 27.5px; color: var(--ink); font-weight: 300; }
  .contact b { color: var(--navy); font-weight: 700; }

  .brand-name {
    position: absolute; left: 563px; top: 1014px;
    font-family: "Barlow Condensed", "Arial Narrow", sans-serif; font-weight: 700;
    font-size: 62px; line-height: 1; color: var(--navy); letter-spacing: 1px; text-transform: uppercase;
  }
</style>
</head>
<body>
<div class="canvas">
  <main class="ad-page">
    <div class="rule rule--top"></div>

    <h1 class="headline">
      <span class="headline__big">Building</span>
      <span class="headline__mid">Your vision for better</span>
      <span class="headline__big headline__big--second">Healthcare</span>
    </h1>

    <div class="strap">Your Partner in Early Phase Clinical Biomanufacturing</div>

    <div class="intro">
      <p>We have been serving the pharmaceutical, biotechnology and veterinary industry for over 20 years so you can create innovative medicines for worldwide health problems.</p>
      <p>Get your therapeutics to the patient faster with cost-effective manufacturing for your GMP clinical trial material. We offer rapid technology transfer, scale-up development and manufacturing of microbial cell-derived proteins at up to 500L scale. We prepare your active pharmaceutical ingredient (API) products to a world class standard ready for clinical development.</p>
    </div>

    <div class="tab tab--products">Products:</div>
    <ul class="offer-list offer-list--products">
      <li>Recombinant proteins</li>
      <li>Live Biotherapeutics</li>
      <li>Bacterial vaccines</li>
      <li>Plasmid DNA</li>
    </ul>

    <div class="tab tab--services">Services:</div>
    <ul class="offer-list offer-list--services">
      <li>Bacterial / Yeast Fermentation</li>
      <li>Cell Banking</li>
      <li>Process Development/Scale-up</li>
      <li>cGMP Manufacture of biopharmaceutical APIs</li>
      <li>Stability Testing</li>
    </ul>

    <svg class="feature-photo" viewBox="0 0 398 398" role="img" aria-label="Photo of two scientists in lab coats working together in a laboratory">
      <defs>
        <radialGradient id="labTone" cx="45%" cy="40%" r="70%">
          <stop offset="0" stop-color="#eef3f8"/>
          <stop offset="0.6" stop-color="#c9d6e3"/>
          <stop offset="1" stop-color="#7f98b0"/>
        </radialGradient>
      </defs>
      <circle cx="199" cy="199" r="186" fill="none" stroke="var(--lime)" stroke-width="26"/>
      <circle cx="199" cy="199" r="161" fill="url(#labTone)"/>
    </svg>

    <div class="contact">
      <div><b>Visit</b> verottbio.com.au</div>
      <div><b>Australia</b> +61(7)30185402</div>
      <div><b>Email</b> enquiries@verottbio.com.au</div>
    </div>

    <div class="brand-name">Verott Bio</div>

    <div class="rule rule--bottom"></div>
  </main>
</div>
</body>
</html>
```